Crest Automotive Reconditioning Business Card

We need a professional business card that features our logo, a picture of the employee, and a brief list of our services.
I've attached a logo, and will attach photos at a later date.
The four services that need to be listed are Bumper repair and repainting, road rash repair, clear coat scratch repair, and automotive touch-up.
Target Market(s)
30 - 40 year male general managers of automobile dealerships. They are used to seeing every vendor gimmick under the sun. This brochure needs to impress with its simplicity and honesty.
Industry/Entity Type
Automotive
Look and feel
Each slider illustrates characteristics of the customer's brand and the style your logo design should communicate.

```html
<!DOCTYPE html>
<html lang="en">
<head>
<meta charset="utf-8">
<title>Crest Automotive Reconditioning – Business Card</title>
<link rel="stylesheet" href="https://fonts.googleapis.com/css2?family=Arimo:wght@400;700&family=Open+Sans:wght@400&display=swap">
<style>
  :root {
    --backdrop: #f05a33;
    --card-cream: #f8f2e3;
    --card-cream-edge: #ece4cf;
    --card-slate: #5e5e5e;
    --card-slate-dark: #4e4e4e;
    --ink-dark: #2a2a2a;
    --ink-label: #333333;
    --accent-red: #e8452c;
    --service-text: #e4e4e4;
    --art-orange: #e0642f;
    --art-slate: #5a5a5a;
  }
  * { margin: 0; padding: 0; box-sizing: border-box; }
  html, body {
    width: 1200px;
    height: 457px;
    overflow: hidden;
    background: var(--backdrop);
  }
  .canvas {
    position: relative;
    width: 1200px;
    height: 457px;
    background: var(--backdrop);
  }
  .card {
    position: absolute;
    top: 64px;
    width: 527px;
    height: 324px;
    box-shadow: 0 1px 3px rgba(0,0,0,0.15);
    overflow: hidden;
  }
  .card-front {
    left: 56px;
    background: radial-gradient(ellipse at 50% 45%, var(--card-cream) 55%, var(--card-cream-edge) 100%);
  }
  .card-back {
    left: 605px;
    background: linear-gradient(160deg, var(--card-slate) 0%, var(--card-slate-dark) 100%);
  }
  .brand-name {
    position: absolute;
    top: 140px;
    left: 0;
    width: 100%;
    display: flex;
    flex-direction: column;
    align-items: center;
    font-family: "Arimo", Arial, sans-serif;
    font-weight: 700;
    color: var(--ink-dark);
    text-transform: uppercase;
  }
  .brand-word {
    font-size: 50px;
    line-height: 52px;
    letter-spacing: 3px;
  }
  .brand-descriptor {
    margin-top: 6px;
    font-size: 14px;
    line-height: 16px;
    letter-spacing: 1px;
  }
  .contact {
    position: absolute;
    top: 244px;
    left: 0;
    width: 100%;
    text-align: center;
    font-family: "Arimo", Arial, sans-serif;
    font-size: 20px;
    line-height: 29px;
    color: var(--ink-label);
  }
  .contact-value { color: var(--accent-red); }
  .mechanic-art {
    position: absolute;
    left: 0;
    top: 0;
    width: 235px;
    height: 324px;
    background: radial-gradient(ellipse 70% 60% at 40% 58%, var(--art-orange) 0%, rgba(224,100,47,0.55) 50%, rgba(90,90,90,0) 100%);
  }
  .services {
    position: absolute;
    left: 262px;
    top: 211px;
    list-style: none;
    font-family: "Open Sans", Arial, sans-serif;
    font-size: 17.5px;
    line-height: 23px;
    color: var(--service-text);
  }
</style>
</head>
<body>
<main class="canvas">
  <section class="card card-front">
    <p class="brand-name">
      <span class="brand-word">Crest</span>
      <span class="brand-descriptor">Automotive Reconditioning</span>
    </p>
    <div class="contact">
      <p>Phone : <span class="contact-value">00000 00000</span></p>
      <p>Email : <span class="contact-value">000000000@crestmail.com</span></p>
    </div>
  </section>
  <section class="card card-back">
    <div class="mechanic-art" role="img" aria-label="Cartoon mechanic in an orange cap and shirt raising a wrench"></div>
    <ul class="services">
      <li>Bumper repair and repainting</li>
      <li>road rash repair</li>
      <li>clear coat scratch repair</li>
      <li>automotive touch-up</li>
    </ul>
  </section>
</main>
</body>
</html>
```